Business Card Design

Please use the Logo for colors and styles, and create a business card using the following info:

Matthias Loeber
Web Developer

Loeber Solutions
+41 76 482 17 05
matthias@loeber-solutions.example
www.loeber-solutions.example

Download the logo at http://loeber-solutions.example/tl_files/loeber_solutions.zip

Thanks for your works!

```html
<!DOCTYPE html>
<html lang="en">
<head>
<meta charset="utf-8">
<title>Loeber Solutions – Business Card</title>
<link rel="stylesheet" href="https://fonts.googleapis.com/css2?family=Jost:wght@400;500;600&display=swap">
<style>
  :root {
    --canvas-bg: #e6eaee;
    --card-navy: #2b5282;
    --brand-blue: #1f7bc1;
    --brand-navy: #1d477a;
    --brand-tint: #d4e5f3;
    --brand-tint-deep: #a9c6e2;
    --ink: #2d2d2d;
    --paper: #ffffff;
    --shadow: rgba(20, 40, 70, 0.18);
  }
  * { box-sizing: border-box; margin: 0; padding: 0; }
  html, body {
    width: 1200px;
    height: 960px;
    overflow: hidden;
    background: var(--canvas-bg);
    font-family: "Jost", "Futura", sans-serif;
  }
  .canvas {
    position: relative;
    width: 1200px;
    height: 960px;
  }
  .card {
    position: absolute;
    left: 250px;
    width: 700px;
    height: 400px;
    box-shadow: 0 12px 30px var(--shadow);
    overflow: hidden;
  }
  .card--front {
    top: 50px;
    background: var(--card-navy);
    display: flex;
    align-items: center;
    justify-content: center;
  }
  .wordmark {
    display: flex;
    align-items: center;
    gap: 14px;
    color: var(--paper);
    font-weight: 500;
    font-size: 46px;
    letter-spacing: 1px;
    text-transform: uppercase;
  }
  .wordmark__dot {
    width: 18px;
    height: 18px;
    border-radius: 50%;
    background: var(--paper);
  }
  .card--back {
    top: 510px;
    background: var(--paper);
  }
  .back__graphic {
    position: absolute;
    left: 0;
    top: 0;
    width: 370px;
    height: 400px;
    background: linear-gradient(135deg, var(--brand-tint) 0%, var(--brand-tint-deep) 100%);
  }
  .back__info {
    position: absolute;
    left: 408px;
    top: 54px;
    width: 270px;
    color: var(--ink);
  }
  .person__name {
    font-size: 26px;
    font-weight: 400;
    letter-spacing: 0.5px;
    line-height: 1.15;
  }
  .person__role {
    font-size: 22px;
    font-weight: 400;
    letter-spacing: 0.5px;
    line-height: 1.2;
  }
  .back__rule {
    border: none;
    border-top: 2px solid var(--brand-navy);
    margin: 14px 0 14px;
    width: 270px;
  }
  .contact-list { list-style: none; }
  .contact-list li {
    display: flex;
    align-items: center;
    gap: 8px;
    font-size: 14.5px;
    line-height: 1.4;
    white-space: nowrap;
  }
  .contact-list svg { flex: none; width: 12px; height: 12px; }
  .contact-list .contact--web {
    font-weight: 600;
    color: var(--brand-navy);
  }
  .address {
    margin-top: 18px;
    font-style: normal;
    font-size: 15px;
    line-height: 1.3;
  }
</style>
</head>
<body>
<main class="canvas">

  <section class="card card--front" aria-label="Card front">
    <div class="wordmark">
      <span class="wordmark__dot" aria-hidden="true"></span>
      <span class="wordmark__name">Loeber Solutions</span>
    </div>
  </section>

  <section class="card card--back" aria-label="Card back">
    <div class="back__graphic" role="img" aria-label="Large blue brand ring graphic"></div>

    <div class="back__info">
      <h1 class="person__name">Matthias Loeber</h1>
      <p class="person__role">Web Developer</p>
      <hr class="back__rule">
      <ul class="contact-list">
        <li>
          <svg viewBox="0 0 12 12" aria-hidden="true"><path d="M3 1 L5 3.2 L4 4.6 Q5 7 7.4 8 L8.8 7 L11 9 L9.8 10.8 Q6 11 3.4 8.4 Q1 6 1.2 2.2 Z" fill="var(--brand-navy)"/></svg>
          <span>+41 76 482 17 05</span>
        </li>
        <li>
          <svg viewBox="0 0 12 12" aria-hidden="true"><rect x="0.5" y="2" width="11" height="8" fill="var(--brand-navy)"/><path d="M0.8 2.4 L6 6.6 L11.2 2.4" fill="none" stroke="#fff" stroke-width="1"/></svg>
          <span>matthias@loeber-solutions.example</span>
        </li>
        <li class="contact--web">
          <svg viewBox="0 0 12 12" aria-hidden="true"><circle cx="6" cy="6" r="5.3" fill="var(--brand-navy)"/><path d="M0.8 6 H11.2 M6 0.8 V11.2 M6 0.8 Q2.8 6 6 11.2 M6 0.8 Q9.2 6 6 11.2" fill="none" stroke="#fff" stroke-width="0.8"/></svg>
          <span>www.loeber-solutions.example</span>
        </li>
      </ul>
      <address class="address">
        Loeber Solutions<br>
        Birkenhaldeweg 12<br>
        CH-8999 Oberbach
      </address>
    </div>
  </section>

</main>
</body>
</html>
```